Advanced Therapeutic Massage Therapist

I need a business card advertising my massage services as an advanced therapeutic massage therapist. I offer advanced therapeutic massage, swedish and deep tissue. I want to create a simple, professional and feminine card. I like bright colours and creativity.

I prefer a bold and experimental approach rather than something status-quo. A card to suggest therapeutic healing through dynamic massage. Motifs, shapes or layout which suggest movement and flow.

Target Market(s)

Everybody!

Industry/Entity Type

Health And Wellness

Contact Information for Business Card

The card should include:
My name, logo, services offered and my contact details.

Siobhán Delaney
Massage Therapist

- Swedish - Deep Tissue - Advanced Therapeutic

Phone: (+353) 87 296 1740
Email: regenerate@siobhandelaney-example.com
Website: www.siobhandelany-example.com

Font styles to use
Serif
Sans Serif
Decorative
Script

Colors

Designer to choose colors to be used in the design.

Requirements
Must have
• An example may contain something like this, yet concise:
• "Siobhán Delaney
• Massage Therapist
• - Swedish - Deep Tissue - Advanced Therapeutic"
Nice to have
• This sentence is optional:
• Imagery such as a logo or symbol. I have attached a file containing a logo I had produced however the name is incorrect now as it is "Siobhán" not "Sadie". It could be edited to change it to Siobhán.
• I have sent the file as .psd .jpg. .pdf and .png
• I like when the card conveys energy, movement, pressure points, flow etc.
• I just like the designer to follow their own style and ideas. I like bright colours but must have a lot of a base colour to offset it. I really prefer them to follow their own inspiration. That is my preference.
Should not have
• Pine trees, non-native trees to Britain and Ireland, exotic flowers or animals that are not native to Britain and Ireland.
• I don't like brown as the background colour of the card.
• The cars shouldn't look like a wedding invitation i.e too many floral type designs.

```html
<!DOCTYPE html>
<html lang="en">
<head>
<meta charset="utf-8">
<title>Siobhán Delaney – Massage Therapist business cards</title>
<link rel="stylesheet" href="https://fonts.googleapis.com/css2?family=Figtree:ital,wght@0,400;1,400&display=swap">
<style>
  :root {
    --paper: #ffffff;
    --card-grey: #ececec;
    --ink: #3a3a3a;
    --pink: #e0607a;
    --magenta: #a31f7c;
    --violet: #6a2a90;
    --navy: #2b2a7e;
    --red: #e2322a;
    --orange: #f5921e;
    --sky: #1c9be2;
    --deep-blue: #1a4aa3;
    --mist: #f2f4f7;
    --leaf: #9ccf8c;
    --green: #3ea35a;
    --brand-tint: #b9d2b4;
    --brand-ink: #6f8a6c;
  }
  * { margin: 0; padding: 0; box-sizing: border-box; }
  html, body { width: 1200px; height: 848px; overflow: hidden; background: var(--paper); }
  body { position: relative; font-family: "Figtree", sans-serif; color: var(--ink); }

  .card {
    position: absolute;
    width: 229px;
    height: 355px;
    overflow: hidden;
    background: var(--card-grey);
  }
  .row-top { top: 49px; }
  .row-bottom { top: 439px; }
  .col-1 { left: 78px; }
  .col-2 { left: 356px; }
  .col-3 { left: 630px; }
  .col-4 { left: 883px; }

  /* artwork placeholders */
  .artwork { position: absolute; inset: 0; }
  .artwork-warm-violet { background: linear-gradient(170deg, var(--pink) 0%, var(--magenta) 50%, var(--violet) 100%); }
  .artwork-blue { background: linear-gradient(200deg, var(--sky) 0%, var(--mist) 50%, var(--deep-blue) 100%); }
  .artwork-sunset { background: linear-gradient(180deg, var(--red) 0%, var(--orange) 30%, var(--magenta) 65%, var(--navy) 100%); }
  .artwork-green { background: linear-gradient(180deg, var(--mist) 0%, var(--leaf) 55%, var(--green) 100%); }
  .artwork-pink-orange { background: linear-gradient(100deg, var(--magenta) 0%, var(--orange) 50%, var(--pink) 100%); }
  .artwork-sun {
    position: absolute; left: 34px; top: 34px; width: 161px; height: 277px;
    background: linear-gradient(180deg, var(--orange) 0%, var(--red) 50%, var(--navy) 100%);
  }

  /* text cards */
  .info p { white-space: nowrap; }
  .brand-mark { display: flex; align-items: center; gap: 6px; }
  .brand-dot { width: 46px; height: 46px; border-radius: 50%; background: var(--brand-tint); flex: none; }
  .brand-name { font-size: 8px; color: var(--brand-ink); white-space: nowrap; }

  .back-a .qualified { position: absolute; left: 25px; top: 70px; font-size: 13px; }
  .back-a .services { position: absolute; left: 25px; top: 121px; font-size: 10.5px; line-height: 1.3; }
  .back-a .brand-mark { position: absolute; left: 30px; top: 218px; }
  .back-a .contact { position: absolute; left: 25px; top: 287px; font-size: 10.5px; line-height: 1.4; }

  .back-b .services { position: absolute; left: 32px; top: 30px; font-size: 13.5px; line-height: 1.3; }
  .back-b .qualified { position: absolute; left: 32px; top: 96px; font-size: 13.5px; }
  .back-b .vertical {
    position: absolute; left: 22px; top: 333px;
    transform: rotate(-90deg); transform-origin: left top;
    font-size: 10.5px; line-height: 1.55;
  }
  .back-b .role { font-style: italic; margin-bottom: 6px; }
  .back-b .brand-mark {
    position: absolute; left: 132px; top: 268px;
    flex-direction: column; gap: 4px;
  }
</style>
</head>
<body>

<!-- Row 1 -->
<section class="card row-top col-1" aria-label="Card front">
  <div class="artwork artwork-warm-violet" role="img" aria-label="Soft blurred colour field in pink, magenta and violet"></div>
</section>

<section class="card row-top col-2" aria-label="Card front">
  <div class="artwork-sun" role="img" aria-label="Sun motif in orange, red and indigo"></div>
</section>

<section class="card row-top col-3" aria-label="Card front">
  <div class="artwork artwork-blue" role="img" aria-label="Soft blurred colour field in sky blue, white and deep blue"></div>
</section>

<section class="card row-top col-4 back-a info" aria-label="Card back, contact details">
  <p class="qualified">Verlow qualified</p>
  <div class="services">
    <p>Swedish</p>
    <p>Deep Tissue</p>
    <p>Advanced Therapeutic</p>
  </div>
  <div class="brand-mark">
    <span class="brand-dot"></span>
    <span class="brand-name">Siobhán Delaney</span>
  </div>
  <div class="contact">
    <p>(+353) 87 296 1740</p>
    <p>siobhan@siobhandelaney-example.com</p>
    <p>www.siobhandelany-example.com</p>
  </div>
</section>

<!-- Row 2 -->
<section class="card row-bottom col-1" aria-label="Card front">
  <div class="artwork artwork-sunset" role="img" aria-label="Soft blurred colour field in red, orange, magenta and indigo"></div>
</section>

<section class="card row-bottom col-2" aria-label="Card front">
  <div class="artwork artwork-green" role="img" aria-label="Soft blurred colour field in white and greens"></div>
</section>

<section class="card row-bottom col-3" aria-label="Card front">
  <div class="artwork artwork-pink-orange" role="img" aria-label="Soft blurred colour field in magenta, orange and pink"></div>
</section>

<section class="card row-bottom col-4 back-b info" aria-label="Card back, services and contact">
  <div class="services">
    <p>Swedish -</p>
    <p>Deep Tissue -</p>
    <p>Advanced Therapeutic</p>
  </div>
  <p class="qualified">Verlow qualified</p>
  <div class="vertical">
    <p>Siobhán Delaney</p>
    <p class="role">Massage Therapist</p>
    <p>(+353) 87 296 1740</p>
    <p>siobhan@siobhandelaney-example.com</p>
    <p>www.siobhandelany-example.com</p>
  </div>
  <div class="brand-mark">
    <span class="brand-dot"></span>
    <span class="brand-name">Siobhán Delaney</span>
  </div>
</section>

</body>
</html>
```